New professional looking flyer for company

I need our flyer updated my flyer is the Lvb flyer Have attached current flyer so you know what services need to be listed. Want it to be in mainly dark colours like black and dark grey with pops of light grey, silver or white. i have added several photos for you to choose which ones work best with your design would like The photos to be in colour for the flyer. But can have a mix of greyscale if that works for your design j have attached another companies flyers as design ideas to show what I am looking for

Target Market(s)

new clients

Industry/Entity Type

transport and earthmoving

Colors

Designer to choose colors to be used in the design.

Requirements
Nice to have
• Look professional
Should not have
• No orange or red or green

```html
<!DOCTYPE html>
<html lang="en">
<head>
<meta charset="utf-8">
<title>Lvb Pty Ltd – Heavy Vehicle Recovery Services Flyer</title>
<link rel="stylesheet" href="https://fonts.googleapis.com/css2?family=Poppins:wght@300;400;500;600;700&family=Saira:ital,wght@1,800;1,900&display=swap">
<style>
  :root{
    --black:#0b0b0c;
    --charcoal:#1c1d1f;
    --silver:#c9ccd0;
    --silver-dark:#8d9095;
    --white:#ffffff;
    --accent:#f3b51b;
  }
  *{margin:0;padding:0;box-sizing:border-box}
  html,body{width:931px;height:1200px;overflow:hidden;background:#d9d9d9}
  .flyer{position:relative;width:931px;height:1200px;background:var(--black);font-family:"Poppins",sans-serif;color:var(--white);overflow:hidden}

  .hero{position:absolute;left:0;top:0;width:931px;height:560px}
  .hero svg{position:absolute;inset:0}

  .brand{position:absolute;left:74px;top:56px;width:214px;text-align:center}
  .brand-rule{height:1px;background:var(--silver-dark);margin-bottom:6px}
  .brand-name{font-family:"Poppins",sans-serif;font-weight:700;font-size:64px;line-height:1;color:var(--silver);letter-spacing:2px}
  .brand-sub{display:flex;align-items:center;gap:8px;margin-top:4px;font-size:14px;color:var(--silver)}
  .brand-sub::before,.brand-sub::after{content:"";flex:1;height:1px;background:var(--silver-dark)}

  .headline{position:absolute;left:62px;top:202px;font-family:"Saira",sans-serif;font-style:italic;font-weight:900;font-size:52px;line-height:47px;text-transform:uppercase;color:var(--white);letter-spacing:.5px}
  .headline span{display:block}
  .headline span:nth-child(2){padding-left:8px}
  .services-tag{position:absolute;left:54px;top:362px;width:270px;height:42px;background:var(--black);transform:skewX(-10deg);display:flex;align-items:center;justify-content:center}
  .services-tag span{transform:skewX(10deg);font-size:28px;letter-spacing:8px;color:var(--accent);font-weight:400}
  .intro{position:absolute;left:70px;top:426px;width:330px;font-size:23px;line-height:29px;font-weight:500}

  .section-title{position:absolute;left:68px;top:598px;font-family:"Saira",sans-serif;font-style:italic;font-weight:900;font-size:38px;letter-spacing:1px;background:linear-gradient(180deg,#f2f2f2 0%,#9c9fa3 55%,#d4d6d9 100%);-webkit-background-clip:text;background-clip:text;color:transparent}
  .service-list{position:absolute;top:658px;list-style:none;font-size:16px;line-height:27.5px}
  .service-list li{display:flex;align-items:center;gap:6px;white-space:nowrap}
  .service-list svg{width:15px;height:15px;flex:none}
  .list-left{left:68px}
  .list-middle{left:387px}
  .list-right{left:597px}

  .gallery{position:absolute;left:0;top:790px;width:931px;height:270px}
  .gallery svg{position:absolute;inset:0}

  .footer{position:absolute;left:0;top:992px;width:931px;height:208px;background:linear-gradient(180deg,#232426 0%,#1a1b1d 100%)}
  .offer{position:absolute;left:62px;top:1024px;font-size:19.8px;font-weight:300;color:var(--accent);white-space:nowrap}
  .cta{position:absolute;left:62px;top:1052px;font-size:25px;font-weight:700;text-transform:uppercase;letter-spacing:-.3px;white-space:nowrap}
  .phone-band{position:absolute;left:0;top:1108px;width:361px;height:46px;background:linear-gradient(90deg,#5a5d61 0%,#c6c8cb 55%,#8e9195 85%,rgba(60,62,65,0) 100%);clip-path:polygon(0 0,100% 0,96% 100%,0 100%)}
  .contact{position:absolute;display:flex;align-items:center;gap:6px;white-space:nowrap}
  .contact svg{flex:none}
  .contact-phone{left:62px;top:1108px;height:46px;font-size:33px;font-weight:700;color:#222326}
  .contact-email{left:378px;top:1116px;height:30px;font-size:22px}
  .contact-web{left:655px;top:1116px;height:30px;font-size:22px}
</style>
</head>
<body>
<main class="flyer">

  <section class="hero">
    <svg width="931" height="560" viewBox="0 0 931 560">
      <defs>
        <linearGradient id="hero-photo-tone" x1="0" y1="0" x2="0" y2="1">
          <stop offset="0" stop-color="#4f86c2"/>
          <stop offset="0.3" stop-color="#a9c4de"/>
          <stop offset="0.48" stop-color="#d9d6cc"/>
          <stop offset="0.56" stop-color="#b89a66"/>
          <stop offset="1" stop-color="#c4a066"/>
        </linearGradient>
        <linearGradient id="panel-tone" x1="0" y1="0" x2="0.4" y2="1">
          <stop offset="0" stop-color="#5c6065"/>
          <stop offset="0.6" stop-color="#6e7277"/>
          <stop offset="1" stop-color="#7b7f84"/>
        </linearGradient>
        <linearGradient id="silver-edge" x1="0" y1="0" x2="1" y2="1">
          <stop offset="0" stop-color="#8a8d91"/>
          <stop offset="0.5" stop-color="#e3e5e8"/>
          <stop offset="1" stop-color="#7d8085"/>
        </linearGradient>
      </defs>
      <rect x="380" y="0" width="551" height="552" fill="url(#hero-photo-tone)" role="img" aria-label="Photo: white road train tanker truck parked on red-dirt outback ground under a blue sky"/>
      <polygon points="0,0 398,0 548,556 0,556" fill="url(#silver-edge)"/>
      <polygon points="0,0 386,0 534,552 0,552" fill="url(#panel-tone)"/>
      <rect x="0" y="552" width="560" height="8" fill="var(--black)"/>
    </svg>

    <div class="brand">
      <div class="brand-rule"></div>
      <div class="brand-name">Lvb</div>
      <div class="brand-sub">Pty Ltd</div>
    </div>

    <h1 class="headline"><span>Heavy</span><span>Vehicle</span><span>Recovery</span></h1>
    <div class="services-tag"><span>SERVICES</span></div>
    <p class="intro">It is a long established fact that a reader will be distracted</p>
  </section>

  <h2 class="section-title">OUR SERVICES</h2>

  <ul class="service-list list-left">
    <li><svg viewBox="0 0 16 16"><circle cx="8" cy="8" r="8" fill="#f3b51b"/><path d="M4.5 8.3l2.3 2.2 4.7-4.8" fill="none" stroke="#fff" stroke-width="1.8" stroke-linecap="round" stroke-linejoin="round"/></svg>Over size loads / Hot Shot Loads</li>
    <li><svg viewBox="0 0 16 16"><circle cx="8" cy="8" r="8" fill="#f3b51b"/><path d="M4.5 8.3l2.3 2.2 4.7-4.8" fill="none" stroke="#fff" stroke-width="1.8" stroke-linecap="round" stroke-linejoin="round"/></svg>Heavy Vehicle Recovery Services</li>
    <li><svg viewBox="0 0 16 16"><circle cx="8" cy="8" r="8" fill="#f3b51b"/><path d="M4.5 8.3l2.3 2.2 4.7-4.8" fill="none" stroke="#fff" stroke-width="1.8" stroke-linecap="round" stroke-linejoin="round"/></svg>Potable Water Deliveries</li>
    <li><svg viewBox="0 0 16 16"><circle cx="8" cy="8" r="8" fill="#f3b51b"/><path d="M4.5 8.3l2.3 2.2 4.7-4.8" fill="none" stroke="#fff" stroke-width="1.8" stroke-linecap="round" stroke-linejoin="round"/></svg>Road Building / Maintenance</li>
  </ul>
  <ul class="service-list list-middle">
    <li><svg viewBox="0 0 16 16"><circle cx="8" cy="8" r="8" fill="#f3b51b"/><path d="M4.5 8.3l2.3 2.2 4.7-4.8" fill="none" stroke="#fff" stroke-width="1.8" stroke-linecap="round" stroke-linejoin="round"/></svg>Road Train Tippers</li>
    <li><svg viewBox="0 0 16 16"><circle cx="8" cy="8" r="8" fill="#f3b51b"/><path d="M4.5 8.3l2.3 2.2 4.7-4.8" fill="none" stroke="#fff" stroke-width="1.8" stroke-linecap="round" stroke-linejoin="round"/></svg>Road Train Tankers</li>
    <li><svg viewBox="0 0 16 16"><circle cx="8" cy="8" r="8" fill="#f3b51b"/><path d="M4.5 8.3l2.3 2.2 4.7-4.8" fill="none" stroke="#fff" stroke-width="1.8" stroke-linecap="round" stroke-linejoin="round"/></svg>Road Train Flat Tops</li>
    <li><svg viewBox="0 0 16 16"><circle cx="8" cy="8" r="8" fill="#f3b51b"/><path d="M4.5 8.3l2.3 2.2 4.7-4.8" fill="none" stroke="#fff" stroke-width="1.8" stroke-linecap="round" stroke-linejoin="round"/></svg>Drop Deck Trailers</li>
  </ul>
  <ul class="service-list list-right">
    <li><svg viewBox="0 0 16 16"><circle cx="8" cy="8" r="8" fill="#f3b51b"/><path d="M4.5 8.3l2.3 2.2 4.7-4.8" fill="none" stroke="#fff" stroke-width="1.8" stroke-linecap="round" stroke-linejoin="round"/></svg>Earthworks</li>
    <li><svg viewBox="0 0 16 16"><circle cx="8" cy="8" r="8" fill="#f3b51b"/><path d="M4.5 8.3l2.3 2.2 4.7-4.8" fill="none" stroke="#fff" stroke-width="1.8" stroke-linecap="round" stroke-linejoin="round"/></svg>Sand &amp; Metal Supply &amp; Cartage</li>
    <li><svg viewBox="0 0 16 16"><circle cx="8" cy="8" r="8" fill="#f3b51b"/><path d="M4.5 8.3l2.3 2.2 4.7-4.8" fill="none" stroke="#fff" stroke-width="1.8" stroke-linecap="round" stroke-linejoin="round"/></svg>Mine Site accredited</li>
    <li><svg viewBox="0 0 16 16"><circle cx="8" cy="8" r="8" fill="#f3b51b"/><path d="M4.5 8.3l2.3 2.2 4.7-4.8" fill="none" stroke="#fff" stroke-width="1.8" stroke-linecap="round" stroke-linejoin="round"/></svg>equipment &amp; Operators</li>
  </ul>

  <div class="footer"></div>

  <section class="gallery">
    <svg width="931" height="270" viewBox="0 0 931 270">
      <defs>
        <linearGradient id="site-photo-tone" x1="0" y1="0" x2="0" y2="1">
          <stop offset="0" stop-color="#2f6fc0"/>
          <stop offset="0.5" stop-color="#6d7f8f"/>
          <stop offset="0.7" stop-color="#9a5a3a"/>
          <stop offset="1" stop-color="#a8683f"/>
        </linearGradient>
        <linearGradient id="truck-mono-tone" x1="0" y1="0" x2="1" y2="1">
          <stop offset="0" stop-color="#6b6d70"/>
          <stop offset="0.5" stop-color="#3a3b3d"/>
          <stop offset="1" stop-color="#1f2022"/>
        </linearGradient>
        <linearGradient id="frame-silver" x1="0" y1="0" x2="1" y2="1">
          <stop offset="0" stop-color="#6e7175"/>
          <stop offset="0.5" stop-color="#c8cace"/>
          <stop offset="1" stop-color="#55585c"/>
        </linearGradient>
      </defs>
      <polygon points="600,-30 931,-30 931,200 596,200" fill="url(#truck-mono-tone)" opacity="0.85" role="img" aria-label="Greyscale photo: front of an oversize-load road train prime mover"/>
      <polygon points="0,2 240,2 262,206 0,206" fill="url(#frame-silver)"/>
      <polygon points="0,10 229,10 248,198 0,198" fill="url(#site-photo-tone)" role="img" aria-label="Photo: dark road train truck beside an excavator on a red-dirt work site"/>
      <polygon points="218,2 568,2 594,206 244,206" fill="url(#frame-silver)"/>
      <polygon points="230,10 557,10 581,198 254,198" fill="url(#site-photo-tone)" role="img" aria-label="Photo: yellow wheel loader tipping into a road train trailer on red-dirt ground"/>
    </svg>
  </section>

  <p class="offer">We offer a large range of services not listed so</p>
  <p class="cta">Call us today for a personalised quote to suit your needs</p>

  <div class="phone-band"></div>
  <div class="contact contact-phone">
    <svg width="24" height="24" viewBox="0 0 24 24"><circle cx="12" cy="12" r="12" fill="#f3b51b"/><path d="M8.2 6.5l2 2.1-1.1 1.6c.8 1.7 2 2.9 3.7 3.7l1.6-1.1 2.1 2-1.2 1.8c-4.3-.4-7.9-4-8.3-8.3z" fill="#fff"/></svg>
    <span>768 5550 4219</span>
  </div>
  <div class="contact contact-email">
    <svg width="16" height="12" viewBox="0 0 16 12"><rect width="16" height="12" rx="1.5" fill="#f3b51b"/><path d="M1 1.5l7 5 7-5" fill="none" stroke="#fff" stroke-width="1.4"/></svg>
    <span>info@lvb.com.au</span>
  </div>
  <div class="contact contact-web">
    <svg width="15" height="15" viewBox="0 0 16 16"><circle cx="8" cy="8" r="7" fill="#f3b51b"/><path d="M1 8h14M8 1c-2.5 2-2.5 12 0 14M8 1c2.5 2 2.5 12 0 14" fill="none" stroke="#fff" stroke-width="1"/></svg>
    <span>www.lvb.com.au</span>
  </div>

</main>
</body>
</html>
```